Tildens Biscuit Barn Website

I need a website for a diner/restaurant that has been established in a farming, oil and industrial community for over 15 years. The website needs to be simple in design, but that should demonstrate the mastery of skills of the designer. Our diner/restaurant is family oriented, patriotic but very rustic
Fb Address is fb.me/TildensBarn

Pictures of the restaurant

https://www.filecrate-example.net/s/qk72hdw01/Tildens_05.jpg

Pictures of About us

https://www.filecrate-example.net/sh/zm40vrt88/AboutUsPhotos

Article about Tilden's
https://www.filecrate-example.net/s/wp31nbx57/TildensBiscuitBarn1.PDF
https://www.filecrate-example.net/s/hy65lcu29/TildensBiscuitBarn2.PDF

Reason: I was slow to update with information.

Reason: I am just getting feedback to the designs posted. I wasn't sure of the limited feedback was limiting designers from submitting designs. That and running a business with 25 employees open 12 hours a day, being here 2 hours prior and 2-3 hours after makes for long days.

I've increased the first place prize and also added funds to the second and third place prizes for your effort.

I just need the files in PSD, not HTML 5 as originally requested. We can handle getting the coding part.

Ill have the contest finalized by Monday. Thanks for your patience.

Target Market(s)

Cross section of adults from 18-35 & 35-55.

Industry/Entity Type

Industrial

Font styles to use
Other font styles liked:
• ff tisa web pro or garamond premier pro

Requirements
Must have
• Must be clean, look nice and not look like an afterthought.
Nice to have
• Please see the last two documents for information about our restaurant, which was featured in our local newspaper.

```html
<!DOCTYPE html>
<html lang="en">
<head>
<meta charset="utf-8">
<title>Tildens Biscuit Barn</title>
<link rel="stylesheet" href="https://fonts.googleapis.com/css2?family=Arvo:wght@400;700&family=Open+Sans:wght@400;700&family=Playball&family=Patrick+Hand+SC&display=swap">
<style>
:root{
  --cream:#efe3cb;
  --cream-light:#f5ecd9;
  --ink:#4a433b;
  --title-grey:#7d7873;
  --wood-dark:#2f2116;
  --wood-mid:#4a3423;
  --plank:#8a5a2b;
  --gold:#e8b437;
  --navy:#1f2638;
  --teal:#2a8197;
  --stone:#66625d;
  --footer:#3a3734;
  --frame:#2c2c2c;
}
*{margin:0;padding:0;box-sizing:border-box}
html,body{width:1200px;height:3232px;overflow:hidden}
body{position:relative;background:var(--cream);font-family:"Open Sans",Arial,sans-serif;color:var(--ink)}
.abs{position:absolute}

/* header */
.site-header{left:0;top:0;width:1200px;height:1258px;background:radial-gradient(ellipse at 50% 30%,var(--cream-light),var(--cream) 70%)}
.brand{left:0;top:210px;width:1200px;display:flex;justify-content:center;align-items:center;gap:18px}
.brand-dot{width:34px;height:34px;border-radius:50%;background:var(--teal)}
.brand-name{font-family:"Arvo",Georgia,serif;font-weight:700;font-size:64px;color:var(--teal)}
.main-nav{left:305px;top:526px;width:590px;height:68px;border-radius:6px;background:linear-gradient(180deg,#a8692c,var(--plank) 50%,#6e421c);display:flex;align-items:center;justify-content:space-around;padding:0 40px;box-shadow:0 3px 6px rgba(0,0,0,.35)}
.main-nav a{color:#fff;text-decoration:none;font-weight:700;font-size:14px;letter-spacing:.5px}
.welcome{left:0;top:632px;width:1200px;text-align:center;font-family:"Arvo",Georgia,serif;font-weight:700;font-size:66px;line-height:76px;color:var(--title-grey);text-shadow:0 3px 0 #5a5550,0 5px 6px rgba(0,0,0,.25)}

.photo-frame{border:22px solid var(--frame);box-shadow:0 8px 18px rgba(0,0,0,.45)}
.about-photo{left:92px;top:850px;width:445px;height:300px;transform:rotate(-4deg);background:linear-gradient(135deg,#9a9a9a,#5c5c5c)}
.section-heading{font-family:"Playball",cursive;font-size:38px;color:var(--ink)}
.body-copy{font-family:Arial,Helvetica,sans-serif;font-size:12px;line-height:22px;color:var(--ink)}
.about-heading{left:610px;top:848px}
.about-copy{left:610px;top:902px;width:410px}
.about-copy p+p{margin-top:22px}

/* menu */
.menu-section{left:0;top:1258px;width:1200px;height:799px;background:linear-gradient(90deg,var(--wood-dark),var(--wood-mid) 30%,#5a412b 50%,var(--wood-mid) 70%,var(--wood-dark))}
.menu-cup{left:560px;top:1290px}
.menu-title{left:0;top:1378px;width:1200px;text-align:center;font-family:"Arvo",Georgia,serif;font-weight:700;font-size:76px;letter-spacing:4px;color:#e9dcc2}
.menu-ribbon{left:463px;top:1455px}
.menu-list{top:1572px;width:330px;list-style:none;font-family:"Patrick Hand SC",cursive;font-size:16px}
.menu-list li{display:flex;height:33.4px;align-items:center}
.menu-list .item{width:188px;color:#fff}
.menu-list .price{color:var(--gold)}
.menu-left{left:278px}
.menu-right{left:663px}

/* history */
.history-section{left:0;top:2057px;width:1200px;height:578px;background:var(--cream)}
.history-photo{left:183px;top:2165px;width:259px;height:355px;border-color:#4b4b4b;background:linear-gradient(160deg,#a5a5a5,#555)}
.history-heading{left:513px;top:2180px}
.history-copy{left:513px;top:2238px;width:530px}
.history-copy .lead{width:268px}
.history-copy p+p{margin-top:14px}
.contact-badge{left:795px;top:2195px;width:210px;height:210px;border-radius:50%;background:var(--navy);color:#fff;text-align:center;padding-top:48px;box-shadow:0 4px 10px rgba(0,0,0,.3);text-decoration:none}
.contact-badge strong{display:block;font-family:Arial,sans-serif;font-style:italic;font-weight:700;font-size:34px;line-height:38px}
.contact-badge span{display:block;margin-top:10px;font-style:italic;font-size:17px}

/* contact */
.contact-section{left:0;top:2635px;width:1200px;height:521px;background:linear-gradient(180deg,#7a756f,var(--stone) 60%,#5a5651)}
.map{left:172px;top:2740px;width:431px;height:345px;border-color:#1e1e1e;outline:8px solid #8d8d8d;background:linear-gradient(135deg,#e6e2d6,#cfcabb)}
.contact-title{left:657px;top:2712px;font-family:"Arvo",Georgia,serif;font-weight:700;font-size:66px;color:#f0e4cc}
.contact-name{left:667px;top:2810px;font-weight:700;font-size:27px;color:#fff;letter-spacing:1px}
.contact-address{left:667px;top:2858px;font-size:18px;line-height:27px;color:#fff}
.contact-line{left:672px;display:flex;align-items:center;gap:16px;color:#fff;font-size:18px}
.contact-line .ring{width:50px;height:50px;border:2px solid #fff;border-radius:50%;display:flex;align-items:center;justify-content:center}
.phone-line{top:2958px}
.email-line{top:3028px}

/* footer */
.site-footer{left:0;top:3156px;width:1200px;height:76px;background:var(--footer)}
.copyright{left:172px;top:3190px;font-size:10px;color:#e6e0d6}
.social{left:820px;top:3175px;display:flex;gap:9px}
.social span{width:27px;height:27px;border-radius:50%;background:#f0ebe2}
</style>
</head>
<body>

<header class="abs site-header"></header>
<div class="abs brand"><span class="brand-dot"></span><span class="brand-name">Tilden's</span></div>
<nav class="abs main-nav">
  <a href="#about">ABOUT US</a><a href="#menu">MENU</a><a href="#location">LOCATION</a><a href="#contact">CONTACT US</a>
</nav>
<h1 class="abs welcome">Welcome to<br>Tildens Biscuit Barn</h1>

<div class="abs photo-frame about-photo" role="img" aria-label="Photo of two guests seated at a diner table"></div>
<h2 class="abs section-heading about-heading" id="about">About Tildens Biscuit Barn</h2>
<div class="abs body-copy about-copy">
  <p>Lorem Ipsum is simply dummy text of the printing and typesetting industry. Lorem Ipsum has been the industry's standard dummy text ever since the 1500s, when an unknown printer took a galley of type and scrambled it to make a type specimen book. It has survived not only five centuries, but also the leap into electronic typesetting, remaining essentially unchanged. It was popularised in the 1960s with the release of Letraset sheets containing</p>
  <p>when an unknown printer took a galley of type and scrambled it to make a type specimen book. It has survived not only five centuries...</p>
</div>

<section class="abs menu-section" id="menu" role="img" aria-label="Dark wooden plank background"></section>
<svg class="abs menu-cup" width="80" height="86" viewBox="0 0 80 86" aria-hidden="true">
  <path d="M30 6c-4 6 4 10 0 16M40 2c-4 7 4 12 0 20M50 6c-4 6 4 10 0 16" stroke="#e9dcc2" stroke-width="3" fill="none"/>
  <path d="M10 34h52v14c0 18-12 30-26 30S10 66 10 48z" fill="#e9dcc2"/>
  <path d="M62 40c12 0 12 16 0 16" stroke="#e9dcc2" stroke-width="5" fill="none"/>
</svg>
<h2 class="abs menu-title">MENU</h2>
<svg class="abs menu-ribbon" width="323" height="70" viewBox="0 0 323 70" aria-label="Select your favorite">
  <path d="M0 14h40v40H0l14-20z" fill="#d8ccb3"/>
  <path d="M323 14h-40v40h40l-14-20z" fill="#d8ccb3"/>
  <path d="M30 8q131-14 263 0v44q-132-14-263 0z" fill="#efe3cb"/>
  <text x="161" y="38" text-anchor="middle" font-family="Arvo,Georgia,serif" font-weight="700" font-size="21" fill="#3a2a1c">Select your favorite</text>
</svg>
<ul class="abs menu-list menu-left">
  <li><span class="item">Teas</span><span class="price">: $3.00</span></li>
  <li><span class="item">Coffeetinis</span><span class="price">: $4.00</span></li>
  <li><span class="item">Refreshers</span><span class="price">: $8.00</span></li>
  <li><span class="item">Classic Hot Coffees</span><span class="price">: $6.00</span></li>
  <li><span class="item">Cold Coffees</span><span class="price">: $2.50</span></li>
  <li><span class="item">Smoothies</span><span class="price">: $8.00</span></li>
  <li><span class="item">Desserts</span><span class="price">: $10.00</span></li>
  <li><span class="item">Choco-Lattes</span><span class="price">: $8.00</span></li>
  <li><span class="item">Sandwich</span><span class="price">: $12.00</span></li>
  <li><span class="item">Pizza Mania</span><span class="price">: $12.50</span></li>
  <li><span class="item">Meal Time Cravers</span><span class="price">: $13.00</span></li>
  <li><span class="item">Any Time Cravers</span><span class="price">: $6.00</span></li>
  <li><span class="item">New Food</span><span class="price">: $6.00</span></li>
</ul>
<ul class="abs menu-list menu-right">
  <li><span class="item">Teas</span><span class="price">: $3.00</span></li>
  <li><span class="item">Coffeetinis</span><span class="price">: $4.00</span></li>
  <li><span class="item">Refreshers</span><span class="price">: $8.00</span></li>
  <li><span class="item">Classic Hot Coffees</span><span class="price">: $6.00</span></li>
  <li><span class="item">Cold Coffees</span><span class="price">: $2.50</span></li>
  <li><span class="item">Smoothies</span><span class="price">: $8.00</span></li>
  <li><span class="item">Desserts</span><span class="price">: $10.00</span></li>
  <li><span class="item">Choco-Lattes</span><span class="price">: $8.00</span></li>
  <li><span class="item">Sandwich</span><span class="price">: $12.00</span></li>
  <li><span class="item">Pizza Mania</span><span class="price">: $12.50</span></li>
  <li><span class="item">Meal Time Cravers</span><span class="price">: $13.00</span></li>
  <li><span class="item">Any Time Cravers</span><span class="price">: $6.00</span></li>
  <li><span class="item">New Food</span><span class="price">: $6.00</span></li>
</ul>

<section class="abs history-section"></section>
<div class="abs photo-frame history-photo" role="img" aria-label="Photo of a young child drinking from a milk bottle"></div>
<h2 class="abs section-heading history-heading">Our History</h2>
<div class="abs body-copy history-copy">
  <p class="lead">Lorem Ipsum is simply dummy text of the printing and typesetting industry. Lorem Ipsum has been the industry's standard dummy text ever since the 1500s, when an unknown printer took a galley of type and scrambled it to make a type specimen book. It has survived not only five centuries, but also the leap into electronic typesetting, remaining</p>
  <p>Lorem Ipsum is simply dummy text of the printing and typesetting industry. Lorem Ipsum has been the industry's standard dummy text ever since the 1500s, when an unknown printer took a galley of type and scrambled it to make a type specimen book. It has survived not only five centuries, but also the leap into electronic typesetting, remaining</p>
</div>
<a class="abs contact-badge" href="#contact"><strong>GET IN<br>TOUCH</strong><span>CONTACT NOW</span></a>

<section class="abs contact-section" id="contact" role="img" aria-label="Faded photo of a town square"></section>
<div class="abs photo-frame map" id="location" role="img" aria-label="Road map showing the diner location"></div>
<h2 class="abs contact-title">Contact</h2>
<p class="abs contact-name">TILDENS BISCUIT BARN</p>
<p class="abs contact-address">120, STREET NAME, STATE NAME,<br>COUNTRY NAME,<br>ZIP CODE : 2530623</p>
<div class="abs contact-line phone-line">
  <span class="ring"><svg width="24" height="24" viewBox="0 0 24 24" aria-hidden="true"><path d="M6.6 10.8a15 15 0 0 0 6.6 6.6l2.2-2.2a1 1 0 0 1 1-.25 11.4 11.4 0 0 0 3.6.57 1 1 0 0 1 1 1V20a1 1 0 0 1-1 1A17 17 0 0 1 3 4a1 1 0 0 1 1-1h3.5a1 1 0 0 1 1 1c0 1.25.2 2.45.57 3.57a1 1 0 0 1-.25 1z" fill="#fff"/></svg></span>
  <span>CALL US : ( 55501 ) 230 118</span>
</div>
<div class="abs contact-line email-line">
  <span class="ring"><svg width="24" height="18" viewBox="0 0 24 18" aria-hidden="true"><rect x="1" y="1" width="22" height="16" fill="#fff"/><path d="M1 1l11 9 11-9" stroke="#66625d" stroke-width="2" fill="none"/></svg></span>
  <span>EMAIL US : tildensbarn@info</span>
</div>

<footer class="abs site-footer"></footer>
<p class="abs copyright">©COPYRIGHT 2014 TILDENS BISCUIT BARN | ALL RIGHTS RESERVED</p>
<div class="abs social" aria-label="Social links"><span></span><span></span><span></span><span></span><span></span><span></span></div>

</body>
</html>
```